Kovalen Spinal Care and Performance

We need new business cards, something more modern, clean. On the back of the card maybe a quote. The Dr. likes, “The doctor of the future will give no medicine, but will interest his patient in the care of the human frame, in diet and in the cause and prevention of disease.” - Walter Brisby. We are open to other suggestions. We are a chiropractic office.

```html
<!DOCTYPE html>
<html lang="en">
<head>
<meta charset="utf-8">
<title>Kovalen Spinal Care and Performance – Business Cards</title>
<link href="https://fonts.googleapis.com/css2?family=Lato:wght@400;700;900&family=Italianno&display=swap" rel="stylesheet">
<style>
  :root{
    --bg:#c8c8c8;
    --paper-top:#ffffff;
    --paper-bottom:#e6e6e6;
    --plum:#361a3a;
    --plum-text:#4a1f55;
    --green:#8db53a;
    --green-dark:#5f7d22;
    --ink:#2b2b2b;
    --rule:#5a6a1e;
  }
  *{margin:0;padding:0;box-sizing:border-box}
  html,body{width:1200px;height:675px;overflow:hidden;background:var(--bg)}
  body{font-family:"Lato",sans-serif;position:relative}
  .card{
    position:absolute;top:183px;width:540px;height:309px;
    background:linear-gradient(160deg,var(--paper-top) 30%,var(--paper-bottom));
    box-shadow:0 6px 16px rgba(0,0,0,.25);overflow:hidden;
  }
  .card--back{left:40px}
  .card--front{left:620px}
  .card__swoosh{position:absolute;inset:0;width:100%;height:100%}
  .brand{color:var(--plum-text);font-weight:700;text-align:center;line-height:1.1}
  .brand__name{font-size:34px;letter-spacing:1px;display:flex;align-items:center;justify-content:center;gap:8px}
  .brand__dot{width:12px;height:12px;border-radius:50%;background:var(--green)}
  .brand__tag{font-size:11px;letter-spacing:1px;text-transform:uppercase;margin-top:2px}
  .card--back .brand{position:absolute;top:38px;left:0;right:0}
  .quote{
    position:absolute;top:115px;left:50px;right:50px;text-align:center;
    font-family:"Italianno",cursive;font-size:25px;line-height:1.05;color:var(--ink);
  }
  .card--front .brand{position:absolute;top:108px;left:20px;width:230px}
  .card--front .brand__name{font-size:30px}
  .card--front .brand__tag{font-size:9.5px}
  .divider{position:absolute;left:270px;top:62px;width:1.5px;height:130px;background:var(--rule)}
  .contact{position:absolute;left:290px;top:64px;color:var(--ink)}
  .contact__name{font-size:17px;font-weight:900;color:var(--plum-text);letter-spacing:.5px}
  .contact__role{font-size:12px;margin-bottom:10px}
  .contact__address{font-size:12px;line-height:1.3;margin-bottom:8px}
  .contact__list{list-style:none;font-size:12px;line-height:1.45}
  .contact__list li{display:flex;align-items:center;gap:7px}
  .contact__list svg{width:11px;height:11px;fill:var(--plum-text)}
</style>
</head>
<body>

<section class="card card--back" aria-label="Card back with quote">
  <svg class="card__swoosh" viewBox="0 0 540 309" preserveAspectRatio="none" aria-hidden="true">
    <defs>
      <linearGradient id="greenBack" x1="0" x2="1">
        <stop offset="0" stop-color="var(--green-dark)"/>
        <stop offset="1" stop-color="var(--green)"/>
      </linearGradient>
    </defs>
    <path d="M0,175 Q110,262 540,272 L540,309 L0,309 Z" fill="var(--plum)"/>
    <path d="M90,228 Q300,292 540,250 L540,270 Q290,300 90,228 Z" fill="#ffffff"/>
    <path d="M140,240 Q330,290 540,252 L540,266 Q310,296 140,240 Z" fill="url(#greenBack)"/>
  </svg>
  <div class="brand">
    <div class="brand__name"><span class="brand__dot"></span>KOVALEN</div>
    <div class="brand__tag">Spinal Care and Performance</div>
  </div>
  <p class="quote">“The doctor of the future will give no medicine, but will interest his patient in the care of the human frame, in diet and in the cause and prevention of disease.” - Walter Brisby.</p>
</section>

<section class="card card--front" aria-label="Card front with contact details">
  <svg class="card__swoosh" viewBox="0 0 540 309" preserveAspectRatio="none" aria-hidden="true">
    <defs>
      <linearGradient id="greenFront" x1="0" x2="1">
        <stop offset="0" stop-color="var(--green-dark)"/>
        <stop offset="1" stop-color="var(--green)"/>
      </linearGradient>
    </defs>
    <path d="M0,175 Q110,262 540,272 L540,309 L0,309 Z" fill="var(--plum)"/>
    <path d="M90,228 Q300,292 540,250 L540,270 Q290,300 90,228 Z" fill="#ffffff"/>
    <path d="M140,240 Q330,290 540,252 L540,266 Q310,296 140,240 Z" fill="url(#greenFront)"/>
  </svg>
  <div class="brand">
    <div class="brand__name"><span class="brand__dot"></span>KOVALEN</div>
    <div class="brand__tag">Spinal Care and Performance</div>
  </div>
  <div class="divider"></div>
  <div class="contact">
    <div class="contact__name">DANA OKAFOR</div>
    <div class="contact__role">Owner</div>
    <div class="contact__address">1280 Larkfield Avenue, Brennmoor<br>NC 2, United States</div>
    <ul class="contact__list">
      <li><svg viewBox="0 0 24 24"><path d="M6.6 10.8a15 15 0 0 0 6.6 6.6l2.2-2.2a1 1 0 0 1 1-.25 11.4 11.4 0 0 0 3.6.57 1 1 0 0 1 1 1V20a1 1 0 0 1-1 1A17 17 0 0 1 3 4a1 1 0 0 1 1-1h3.5a1 1 0 0 1 1 1c0 1.25.2 2.45.57 3.6a1 1 0 0 1-.25 1z"/></svg>000-000-000-000</li>
      <li><svg viewBox="0 0 24 24"><path d="M6 2h12v5H6zM4 8h16a2 2 0 0 1 2 2v7h-4v5H6v-5H2v-7a2 2 0 0 1 2-2zm4 8v4h8v-4z"/></svg>000-000-000-000</li>
      <li><svg viewBox="0 0 24 24"><path d="M2 5h20v14H2zm2 2v.5l8 5 8-5V7z"/></svg>info@kovalenspine.com</li>
      <li><svg viewBox="0 0 24 24"><path d="M12 2a10 10 0 1 0 0 20 10 10 0 0 0 0-20zm6.9 9h-3a15 15 0 0 0-1.3-6A8 8 0 0 1 18.9 11zM12 4c.9 1.2 1.7 3.9 1.9 7h-3.8c.2-3.1 1-5.8 1.9-7zM9.4 5a15 15 0 0 0-1.3 6h-3A8 8 0 0 1 9.4 5zM5.1 13h3a15 15 0 0 0 1.3 6 8 8 0 0 1-4.3-6zM12 20c-.9-1.2-1.7-3.9-1.9-7h3.8c-.2 3.1-1 5.8-1.9 7zm2.6-1a15 15 0 0 0 1.3-6h3a8 8 0 0 1-4.3 6z"/></svg>www.kovalenspine.com</li>
    </ul>
  </div>
</section>

</body>
</html>
```